The design should be a multi-page, foldable flyer with the logo and the product name on the front and the web address on the back.
MuLOTI is a word play on "zebra", which the design should reflect in some way.

Target Market(s)

Schools and individual teachers

Industry/Entity Type

Product

Colors
ffffff
000000

```html
<!DOCTYPE html>
<html lang="en">
<head>
<meta charset="utf-8">
<title>MuLOTI Flyer</title>
<link rel="stylesheet" href="https://fonts.googleapis.com/css2?family=Roboto:wght@400;500&family=Roboto+Condensed:wght@400;700&display=swap">
<style>
  :root {
    --black: #000000;
    --white: #ffffff;
    --paper: #f4f4f4;
    --stripe: #d9d9d9;
    --ink: #222222;
    --logo-grey: #444444;
    --stage: #e8e8e8;
    --create: #0f9a3c;
    --perform: #1a9ad9;
    --revise: #e4530f;
    --analyze: #2b2470;
    --administrate: #000000;
    --shade: #9a9a9a;
  }
  * { box-sizing: border-box; margin: 0; padding: 0; }
  html, body { width: 802px; height: 1200px; overflow: hidden; }
  body {
    position: relative;
    background: var(--stage);
    font-family: "Roboto Condensed", "Arial Narrow", sans-serif;
    color: var(--ink);
  }
  .panel {
    position: absolute;
    width: 240px;
    height: 380px;
    box-shadow: 0 4px 14px rgba(0,0,0,.18);
    overflow: hidden;
  }
  .front-cover { left: 140px; top: 40px; background: var(--white); }
  .back-cover { left: 422px; top: 40px; background: var(--black); }
  .panel svg { position: absolute; inset: 0; }

  .cover-brand {
    position: absolute;
    left: 30px;
    top: 150px;
    display: flex;
    align-items: center;
    gap: 10px;
  }
  .cover-brand .dot {
    width: 26px; height: 26px; border-radius: 50%;
    background: var(--logo-grey);
  }
  .cover-brand .name {
    font-family: "Roboto", sans-serif;
    font-size: 38px;
    font-weight: 400;
    color: var(--logo-grey);
    letter-spacing: 1px;
    line-height: 46px;
  }
  .cover-tagline {
    position: absolute;
    left: 66px;
    top: 198px;
    font-size: 7.5px;
    white-space: nowrap;
    color: var(--logo-grey);
  }

  .back-brand {
    position: absolute;
    left: 0; right: 0;
    top: 152px;
    text-align: center;
    font-family: "Roboto", sans-serif;
    font-size: 26px;
    color: var(--logo-grey);
  }
  .web-address {
    position: absolute;
    left: 0; right: 0;
    bottom: 26px;
    text-align: center;
    font-family: "Roboto Condensed", sans-serif;
    font-size: 15px;
    color: var(--white);
    letter-spacing: .5px;
  }

  .spread {
    position: absolute;
    left: 101px;
    top: 460px;
    width: 600px;
    height: 600px;
    display: flex;
    box-shadow: 0 4px 14px rgba(0,0,0,.18);
  }
  .page {
    position: relative;
    width: 300px;
    height: 600px;
    background: linear-gradient(160deg, var(--paper) 0%, var(--stripe) 50%, var(--paper) 100%);
  }
  .page-left { border-right: 1px solid #cfcfcf; }

  .module { position: absolute; left: 28px; width: 252px; }
  .module-head { position: relative; height: 54px; margin-bottom: 8px; }
  .module-head svg { position: absolute; left: 0; top: 0; }
  .module-title {
    position: absolute;
    left: 26px;
    top: 22px;
    font-family: "Roboto", sans-serif;
    font-weight: 500;
    font-size: 19px;
    letter-spacing: 3px;
    color: var(--ink);
  }
  .module-title .on-shape { color: var(--white); }
  .module p {
    font-size: 9.6px;
    line-height: 1.33;
    color: var(--ink);
  }
  .module p b { font-weight: 700; }

  .element-list {
    list-style: none;
    display: grid;
    grid-template-columns: 1fr 1fr;
    grid-auto-flow: column;
    grid-template-rows: repeat(6, 19.5px);
    margin-top: 14px;
    font-size: 9.6px;
  }
  .element-list li { display: flex; align-items: center; gap: 7px; }
  .element-list li::before {
    content: "";
    width: 9px; height: 9px;
    border: 1.5px solid #555;
    border-radius: 50%;
  }

  .create { top: 26px; }
  .perform { top: 375px; }
  .revise { top: 22px; }
  .analyze { top: 228px; }
  .administrate { top: 378px; }
</style>
</head>
<body>

  <section class="panel front-cover">
    <svg width="240" height="380" viewBox="0 0 240 380">
      <polygon points="0,0 240,0 240,20 0,120" fill="#8aa3b2" role="img" aria-label="Photo of students and a teacher at computers"/>
      <polygon points="0,120 240,20 240,48 0,150" fill="var(--black)"/>
      <path d="M0,150 A40,80 0 0 1 0,300" fill="none" stroke="var(--black)" stroke-width="8"/>
      <polygon points="0,290 240,220 240,250 0,322" fill="var(--black)"/>
      <polygon points="40,380 240,300 240,380" fill="var(--stripe)" role="img" aria-label="Zebra stripe pattern"/>
      <polygon points="40,345 230,282 232,372 50,376" fill="#b9b1a0" role="img" aria-label="Colourful bar chart standing on a printed map"/>
    </svg>
    <div class="cover-brand"><span class="dot"></span><span class="name">MuLOTI</span></div>
    <div class="cover-tagline">Tests, Tasks, Marks &amp; Reports in One Place</div>
  </section>

  <section class="panel back-cover">
    <svg width="240" height="380" viewBox="0 0 240 380">
      <circle cx="120" cy="166" r="170" fill="#e4e4e4"/>
      <circle cx="120" cy="166" r="146" fill="var(--black)"/>
      <circle cx="120" cy="166" r="120" fill="#e4e4e4"/>
      <circle cx="120" cy="166" r="98" fill="var(--black)"/>
      <circle cx="120" cy="166" r="80" fill="#dcdcdc"/>
      <rect x="0" y="330" width="240" height="50" fill="var(--black)"/>
    </svg>
    <div class="back-brand">MuLOTI</div>
    <div class="web-address">www.muloti-edu.com</div>
  </section>

  <section class="spread">
    <div class="page page-left" role="img" aria-label="Soft zebra stripe pattern background">
      <article class="module create">
        <div class="module-head">
          <svg width="80" height="54"><polygon points="12,8 78,0 70,54 0,48" fill="var(--shade)" transform="translate(3,3)"/><polygon points="12,8 78,0 70,54 0,48" fill="var(--create)"/></svg>
          <h2 class="module-title"><span class="on-shape">CREA</span>TE</h2>
        </div>
        <p>The <b>CREATE-Module</b> lets you manage your Tasks and Tests easily by providing repositories in which they reside.<br>By continuously expanding the Task-Repository you can reduce the workload for each new Test you create by being able to reuse and adjust existing Tasks.<br>At the moment Tasks can contain the following elements:</p>
        <ul class="element-list">
          <li>Free Text</li>
          <li>Word-/Sentence Gap</li>
          <li>Descriptions</li>
          <li>Math Containers</li>
          <li>Multiple Choice</li>
          <li>Short Answers</li>
          <li>True-False-Justification</li>
          <li>Images</li>
          <li>Audio Files</li>
          <li>Sentence Matching</li>
          <li>Headings</li>
        </ul>
      </article>

      <article class="module perform">
        <div class="module-head">
          <svg width="80" height="54"><polygon points="12,8 78,0 70,54 0,48" fill="var(--shade)" transform="translate(3,3)"/><polygon points="12,8 78,0 70,54 0,48" fill="var(--perform)"/></svg>
          <h2 class="module-title"><span class="on-shape">PERF</span>ORM</h2>
        </div>
        <p>The <b>PERFORM-Module</b> lets your students perform the tests you created. During sessions you are able to monitor what students are producing and you can also pause or stop tests for individual students – for example if you suspect that someone is cheating - or the entire class. The system also keeps track of where students are situated during tests, in order for you to be able reveal cheating attempts afterwards.</p>
      </article>
    </div>

    <div class="page page-right" role="img" aria-label="Soft zebra stripe pattern background">
      <article class="module revise">
        <div class="module-head">
          <svg width="80" height="54"><polygon points="12,8 78,0 70,54 0,48" fill="var(--shade)" transform="translate(3,3)"/><polygon points="12,8 78,0 70,54 0,48" fill="var(--revise)"/></svg>
          <h2 class="module-title"><span class="on-shape">REVI</span>SE</h2>
        </div>
        <p>With the <b>REVISE-Module</b> you can mark the tests previously performed by your students. A lot of different types of tasks can be auto-marked by the system – e.g. Multiple Choice, Short Answers, etc. – freeing you up to concentrate on marking textual work.<br>When marking texts, you can define your own custom error types, allowing you to personalize your markings and to give students the best possible feedback.</p>
      </article>

      <article class="module analyze">
        <div class="module-head">
          <svg width="80" height="54"><polygon points="12,8 78,0 70,54 0,48" fill="var(--shade)" transform="translate(3,3)"/><polygon points="12,8 78,0 70,54 0,48" fill="var(--analyze)"/></svg>
          <h2 class="module-title"><span class="on-shape">ANAL</span>YZE</h2>
        </div>
        <p>The <b>ANALYZE-Module</b> provides several different reports and tools that help you understand the data within your system, like how student performance has changed over time in general or how they perform on specific tasks, tests or even subjects</p>
      </article>

      <article class="module administrate">
        <div class="module-head">
          <svg width="80" height="54"><polygon points="12,8 78,0 70,54 0,48" fill="var(--shade)" transform="translate(3,3)"/><polygon points="12,8 78,0 70,54 0,48" fill="var(--administrate)"/></svg>
          <h2 class="module-title"><span class="on-shape">ADMI</span>NISTRATE</h2>
        </div>
        <p>The <b>ADMINISTRATE-Module</b> contains all administrative data you need within the system. Here you can create, update and delete users, assign them different roles and rights that govern what they are and are not allowed to do and manage your subjects and classes.</p>
      </article>
    </div>
  </section>

</body>
</html>
```